Business Card Design Project

Company Name - Larkmere Med

Wellness consulting and training company. Run through a medical centre.

Main colour themes are orange and blue, as in the logo. Want to replicate same effect with business cards.

To give a sense of freedom and potential as per the company name.

Want the business card to be in line with stationary design, which I have launched as well.

Double sided with design and colour on one side and details on other side.
Updates

Reason: Need business card and stationary design to be teed up.

Target Market(s)

35 to 65 age group.
New age and trendy

Industry/Entity Type

Training

Requirements
Must have
• Colours orange and blue as per logo
Nice to have
• Design to be similar to stationary design, letterhead and envelopes

```html
<!DOCTYPE html>
<html lang="en">
<head>
<meta charset="utf-8">
<title>Larkmere Med Stationery</title>
<link href="https://fonts.googleapis.com/css2?family=Arimo:wght@400;700&family=Oswald:wght@300&family=Allura&display=swap" rel="stylesheet">
<style>
  :root {
    --bg-dark: #2f2f2f;
    --bg-mid: #454545;
    --paper: #ffffff;
    --brand-blue: #1b5fad;
    --band-blue: #0a4fa8;
    --band-blue-light: #2f6fc0;
    --brand-orange: #f26522;
    --ink: #1e1e1e;
    --ink-soft: #444444;
  }
  * { margin: 0; padding: 0; box-sizing: border-box; }
  html, body { width: 1200px; height: 726px; overflow: hidden; }
  body {
    background: radial-gradient(ellipse at 40% 40%, var(--bg-mid), var(--bg-dark));
    font-family: "Arimo", Arial, sans-serif;
    color: var(--ink);
    position: relative;
  }
  .sheet {
    position: absolute;
    background: var(--paper);
    box-shadow: 0 2px 6px rgba(0,0,0,.55);
    overflow: hidden;
  }
  .wordmark {
    position: absolute;
    font-family: "Oswald", "Arial Narrow", sans-serif;
    font-weight: 300;
    color: var(--brand-blue);
    white-space: nowrap;
    line-height: 1;
  }
  .wordmark.on-blue { color: #ffffff; }
  .accent { color: var(--brand-orange); }
  .brand { color: var(--brand-blue); }

  /* Letterhead */
  .letterhead { left: 36px; top: 19px; width: 527px; height: 683px; }
  .letterhead .wordmark { left: 50px; top: 58px; font-size: 26px; }
  .contact-list { position: absolute; left: 363px; top: 53px; font-size: 9px; color: var(--ink-soft); list-style: none; line-height: 11px; }
  .contact-list li { display: flex; align-items: center; gap: 5px; }
  .contact-list svg { width: 8px; height: 8px; fill: var(--brand-blue); }
  .letter-body { position: absolute; left: 50px; top: 148px; width: 426px; font-size: 10.3px; line-height: 11.7px; }
  .letter-body p { margin-bottom: 11.7px; text-align: justify; }
  .letter-body .recipient { font-weight: 700; }
  .letter-body .text-block { margin-top: 23px; }
  .signature { font-family: "Allura", cursive; font-size: 22px; margin-top: 6px; }
  .letter-footer {
    position: absolute; left: 0; bottom: 0; width: 100%; height: 52px;
    background: linear-gradient(180deg, var(--band-blue), var(--band-blue-light));
    color: #fff; font-size: 10.4px; text-align: center; line-height: 50px; letter-spacing: .3px;
  }

  /* Envelope back */
  .envelope-back { left: 608px; top: 19px; width: 526px; height: 265px; }
  .envelope-back svg.flap { position: absolute; left: 0; top: 0; }
  .envelope-back .wordmark { left: 216px; top: 44px; font-size: 22px; }

  /* Envelope front */
  .envelope-front { left: 608px; top: 293px; width: 529px; height: 265px; }
  .envelope-front .wordmark { left: 33px; top: 63px; font-size: 26px; }
  .return-address { position: absolute; left: 33px; top: 198px; font-size: 10px; line-height: 12px; color: var(--ink-soft); }
  .return-address .brand { display: block; }
  .envelope-front .web { position: absolute; right: 50px; top: 222px; font-size: 10px; color: var(--ink-soft); }

  /* Business card front */
  .card-front { left: 608px; top: 567px; width: 235px; height: 134px; background: linear-gradient(160deg, var(--band-blue-light), var(--band-blue)); }
  .card-front .wordmark { left: 0; width: 100%; text-align: center; top: 60px; font-size: 22px; }
  .card-front .web { position: absolute; left: 0; width: 100%; text-align: center; top: 115px; font-size: 7px; color: #fff; }

  /* Business card back */
  .card-back { left: 862px; top: 567px; width: 235px; height: 134px; }
  .card-back .wordmark { left: 24px; top: 64px; font-size: 18px; }
  .card-details { position: absolute; left: 142px; top: 33px; font-size: 5.4px; line-height: 6.6px; color: var(--ink-soft); }
  .card-details .name { font-size: 7.5px; font-weight: 700; color: var(--brand-blue); line-height: 8px; }
  .card-details .role { color: var(--brand-orange); margin-bottom: 9px; }
  .card-details .block { margin-bottom: 6px; }
  .card-details ul { list-style: none; }
  .card-details li { display: flex; align-items: center; gap: 3px; }
  .card-details svg { width: 5px; height: 5px; fill: var(--brand-blue); }
</style>
</head>
<body>

<svg width="0" height="0" style="position:absolute">
  <defs>
    <symbol id="icon-phone" viewBox="0 0 10 10"><path d="M1 3 C1 1.5 2 1 5 1 C8 1 9 1.5 9 3 L7 3.6 L6.5 2.6 L3.5 2.6 L3 3.6 Z M2.5 4.5 L7.5 4.5 L8.5 9 L1.5 9 Z"/></symbol>
    <symbol id="icon-mail" viewBox="0 0 10 10"><path d="M0.5 2 H9.5 V8 H0.5 Z M1.2 2.6 L5 5.6 L8.8 2.6" fill="currentColor"/><path d="M1.2 2.6 L5 5.6 L8.8 2.6" stroke="#fff" stroke-width="0.9" fill="none"/></symbol>
    <symbol id="icon-globe" viewBox="0 0 10 10"><circle cx="5" cy="5" r="4.5"/><path d="M0.5 5 H9.5 M5 0.5 V9.5 M5 0.5 C2.5 3 2.5 7 5 9.5 M5 0.5 C7.5 3 7.5 7 5 9.5 M1.5 2.8 H8.5 M1.5 7.2 H8.5" stroke="#fff" stroke-width="0.6" fill="none"/></symbol>
  </defs>
</svg>

<section class="sheet letterhead">
  <div class="wordmark">Larkmere Med</div>
  <ul class="contact-list">
    <li><svg><use href="#icon-phone"/></svg>555.010.2040</li>
    <li><svg><use href="#icon-mail"/></svg>info@larkmeremed.com</li>
    <li><svg><use href="#icon-globe"/></svg>www.<span class="brand">Larkmere</span><span class="accent">Med</span>.com</li>
  </ul>
  <div class="letter-body">
    <p>Date</p>
    <p class="recipient">Recepient Name</p>
    <p>Company Name<br>Street Address<br>City, State, Zip</p>
    <div class="text-block">
      <p>Lorem ipsum dolor sit amet, consectetuer adipiscing elit, sed diam nonummy nibh euismod tincidunt ut laoreet dolore magna aliquam erat volutpat. Ut wisi enim ad minim veniam, quis nostrud exerci tation ullamcorper suscipit lobortis nisl ut aliquip ex ea commodo consequat. Duis autem vel eum iriure dolor in hendrerit in vulputate velit.</p>
      <p>Nam liber tempor cum soluta nobis eleifend option congue nihil imperdiet doming id quod mazim placerat facer possim assum. Typi non habent claritatem insitam; est usus legentis in iis qui facit eorum claritatem. Investigationes demonstraverunt lectores legere me lius quod ii legunt saepius. Claritas est etiam processus dynamicus, qui sequitur mutationem consuetudium lectorum. Mirum est notare quam littera gothica, quam nunc putamus parum claram, anteposuerit litterarum formas humanitatis per seacula quarta.</p>
      <p>Typi non habent claritatem insitam; est usus legentis in iis qui facit eorum claritatem. Investigationes demonstraverunt lectores legere me lius quod ii legunt saepius. Claritas est etiam processus dynamicus, qui sequitur mutationem consuetudium lectorum. Mirum est notare quam littera gothica, quam nunc putamus parum claram, anteposuerit litterarum formas humanitatis per seacula quarta. Typi non habent claritatem insitam; est usus legentis in iis qui facit eorum claritatem. Investigationes demonstraverunt lectores legere me lius quod ii legunt saepius. Claritas est etiam processus dynamicus, qui sequitur mutationem consuetudium lectorum. Mirum est notare quam littera gothica, quam nunc putamus parum claram, anteposuerit litterarum formas humanitatis per seacula quarta.</p>
    </div>
    <p class="signature">Owen Hale</p>
  </div>
  <footer class="letter-footer">Suite 123, Street Name, State, Zip 1234, Country</footer>
</section>

<section class="sheet envelope-back">
  <svg class="flap" width="526" height="265" viewBox="0 0 526 265">
    <defs>
      <linearGradient id="flap-fill" x1="0" y1="0" x2="0" y2="1">
        <stop offset="0" stop-color="#0a4fa8"/>
        <stop offset="1" stop-color="#1f62b6"/>
      </linearGradient>
    </defs>
    <path d="M0 0 H526 L518 4 C510 40 500 56 470 62 C400 72 320 76 270 86 C250 88 230 86 205 80 C140 66 70 62 36 54 C18 48 12 30 8 4 Z" fill="url(#flap-fill)"/>
  </svg>
  <div class="wordmark on-blue">Larkmere Med</div>
</section>

<section class="sheet envelope-front">
  <div class="wordmark">Larkmere Med</div>
  <address class="return-address" style="font-style:normal">
    <span class="brand">Larkmere Med</span>
    Suite 123, Street Name<br>State, Zip 1234, Country
  </address>
  <div class="web">www.<span class="brand">Larkmere</span><span class="accent">Med</span>.com</div>
</section>

<section class="sheet card-front">
  <div class="wordmark on-blue">Larkmere Med</div>
  <div class="web">www.LarkmereMed.com</div>
</section>

<section class="sheet card-back">
  <div class="wordmark">Larkmere Med</div>
  <div class="card-details">
    <div class="name">Nora Vance</div>
    <div class="role">Managing Director</div>
    <div class="block">Suite 123, Street Name<br>State, Zip 1234, Country</div>
    <ul>
      <li><svg><use href="#icon-phone"/></svg>555.010.2040</li>
      <li><svg><use href="#icon-mail"/></svg>info@larkmeremed.com</li>
      <li><svg><use href="#icon-globe"/></svg>www.<span class="brand">Larkmere</span><span class="accent">Med</span>.com</li>
    </ul>
  </div>
</section>

</body>
</html>
```